Tervolan Pty Ltd professional business card

A professional business card template using the colours from the supplied logo.
Clean crisp lines while, Modern while not being over the top.

Target Market(s)

Construction, commerical and industrial

Industry/Entity Type

Communications

Contact Information for Business Card

For a Communications, IT, Optical fibre installation company

Colors
37b8a4

```html
<!DOCTYPE html>
<html lang="en">
<head>
<meta charset="utf-8">
<title>Tervolan Pty Ltd – Business Card</title>
<link href="https://fonts.googleapis.com/css2?family=Montserrat:wght@400;500;600&display=swap" rel="stylesheet">
<style>
  :root {
    --teal: #138f9f;
    --teal-soft: #2b99a6;
    --teal-text: #1a95a3;
    --grey: #66676b;
    --ink: #3f4044;
    --paper: #ffffff;
    --mist: #dce6e8;
    --mist-grey: #e2e0e1;
    --backdrop: #e9e6e1;
  }
  * { margin: 0; padding: 0; box-sizing: border-box; }
  html, body { width: 1200px; height: 965px; overflow: hidden; }
  body {
    background: var(--backdrop);
    font-family: "Montserrat", sans-serif;
    position: relative;
  }
  .card {
    position: absolute;
    left: 278px;
    width: 647px;
    height: 369px;
    border-radius: 24px;
    overflow: hidden;
    box-shadow: 0 6px 14px rgba(0,0,0,0.18);
  }
  .card--back { top: 96px; background: var(--teal); }
  .card--front { top: 504px; background: var(--paper); }

  .back-texture {
    position: absolute;
    inset: 0;
    background:
      repeating-linear-gradient(180deg, rgba(255,255,255,0) 0 18px, rgba(255,255,255,0.05) 18px 60px, rgba(255,255,255,0) 60px 78px),
      linear-gradient(135deg, var(--teal-soft), var(--teal) 70%);
  }
  .back-wordmark {
    position: absolute;
    left: 326px;
    top: 228px;
    font-size: 50px;
    font-weight: 500;
    color: var(--paper);
    letter-spacing: 1px;
  }

  .front-decor {
    position: absolute;
    left: 270px;
    top: 24px;
    right: 0;
    bottom: 0;
    background:
      linear-gradient(90deg, var(--paper) 0%, rgba(255,255,255,0) 35%),
      linear-gradient(160deg, var(--mist) 0%, var(--mist) 55%, var(--mist-grey) 100%);
    border-top-left-radius: 60% 100%;
  }
  .front-wordmark {
    position: absolute;
    left: 32px;
    top: 30px;
    font-size: 56px;
    font-weight: 500;
    color: var(--grey);
    letter-spacing: 1px;
    line-height: 1;
  }
  .edge-tab {
    position: absolute;
    left: 0;
    top: 144px;
    width: 6px;
    height: 38px;
    background: var(--teal);
    border-radius: 0 4px 4px 0;
  }
  .person-name {
    position: absolute;
    left: 33px;
    top: 142px;
    font-size: 24px;
    font-weight: 600;
    color: var(--teal-text);
    letter-spacing: 0.5px;
  }
  .person-role {
    position: absolute;
    left: 33px;
    top: 172px;
    font-size: 14px;
    font-weight: 500;
    color: var(--ink);
  }
  .address {
    position: absolute;
    left: 33px;
    top: 210px;
    font-size: 17px;
    line-height: 23px;
    color: var(--grey);
    font-style: normal;
  }
  .contact-list {
    position: absolute;
    left: 33px;
    top: 268px;
    list-style: none;
  }
  .contact-list li {
    display: flex;
    align-items: center;
    height: 24px;
    font-size: 17px;
    color: var(--ink);
  }
  .contact-list svg { width: 16px; height: 16px; margin-right: 10px; flex: none; }
</style>
</head>
<body>
  <section class="card card--back" aria-label="Card back">
    <div class="back-texture" role="img" aria-label="Faint repeating brand pattern on teal"></div>
    <div class="back-wordmark">Tervolan</div>
  </section>

  <section class="card card--front" aria-label="Card front">
    <div class="front-decor" role="img" aria-label="Large faint brand decoration"></div>
    <div class="front-wordmark">Tervolan</div>
    <span class="edge-tab"></span>
    <h1 class="person-name">DANIEL HARWOOD</h1>
    <p class="person-role">Director</p>
    <address class="address">Calle Verano 42,<br>2210-118 NJ</address>
    <ul class="contact-list">
      <li>
        <svg viewBox="0 0 16 16" aria-hidden="true"><path fill="#138f9f" d="M3.6 1.5l2.3 2.6-1.3 1.7c.9 2 2.6 3.7 4.6 4.6l1.7-1.3 2.6 2.3-1.3 2.1C7.2 15.3.7 8.8 1.5 3z"/></svg>
        555-284-1937
      </li>
      <li>
        <svg viewBox="0 0 16 16" aria-hidden="true"><rect x="1" y="3" width="14" height="10" fill="#138f9f"/><path d="M1 3l7 5.5L15 3" fill="none" stroke="#fff" stroke-width="1.2"/></svg>
        daniel@tervolan.com
      </li>
      <li>
        <svg viewBox="0 0 16 16" aria-hidden="true"><circle cx="8" cy="8" r="7" fill="#138f9f"/><path d="M1 8h14M8 1c-3 3.5-3 10.5 0 14M8 1c3 3.5 3 10.5 0 14" fill="none" stroke="#fff" stroke-width="1"/></svg>
        www.tervolan.com
      </li>
    </ul>
  </section>
</body>
</html>
```